Letterhead Design Project

We are looking for a simple letterhead design that reflects our core purpose. We help our clients gain clarity and focus but we are there to help them execute. The letterhead design would mainly be utilised for engagement letters and contracts.

Target Market(s)

The customers of our business are large corporate organisations.

Requirements
Must have
• The letterhead must have the company logo
The font used must tie in to the font used in the company logo

Must have the following business details
Address: Level 10, 27 Harlow Lane, Melbourne, Australia, 3000
Phone: +61 3 527 948 183
Fax: +61 3 9042 5317
Website: www.bovrin-u.com.au
Twiiter: @bovrin_u

```html
<!DOCTYPE html>
<html lang="en">
<head>
<meta charset="utf-8">
<title>Bovrin-u Letterhead</title>
<link rel="stylesheet" href="https://fonts.googleapis.com/css2?family=Open+Sans:wght@400;600&display=swap">
<style>
  :root {
    --backdrop: #c9cfcf;
    --paper: #ffffff;
    --ink: #222428;
    --brand-blue: #1a6fd1;
    --watermark: #e6e8e8;
  }
  html, body {
    margin: 0;
    width: 1200px;
    height: 1000px;
    overflow: hidden;
    background: var(--backdrop);
    font-family: "Open Sans", Arial, sans-serif;
    color: var(--ink);
  }
  .letterhead {
    position: absolute;
    left: 267px;
    top: 30px;
    width: 666px;
    height: 940px;
    background: var(--paper);
    box-shadow: 0 4px 14px rgba(0,0,0,0.12);
    overflow: hidden;
  }
  .brand {
    position: absolute;
    left: 60px;
    top: 132px;
    display: flex;
    align-items: center;
    gap: 8px;
  }
  .brand-name {
    font-size: 30px;
    font-weight: 400;
    color: var(--brand-blue);
    letter-spacing: 0.5px;
  }
  .brand-dot {
    width: 20px;
    height: 20px;
    border-radius: 50%;
    background: var(--brand-blue);
  }
  .sender-address {
    position: absolute;
    right: 60px;
    top: 52px;
    font-size: 11px;
    line-height: 1.35;
    text-align: right;
    font-weight: 600;
  }
  .letter-date {
    position: absolute;
    right: 60px;
    top: 112px;
    font-size: 11px;
    font-weight: 600;
  }
  .letter-body {
    position: absolute;
    left: 60px;
    top: 220px;
    width: 540px;
    font-size: 13px;
    line-height: 1.5;
  }
  .letter-body p { margin: 0 0 18px; }
  .signature p { margin: 0 0 22px; }
  .watermark {
    position: absolute;
    right: -40px;
    bottom: 150px;
  }
  .contact-footer {
    position: absolute;
    right: 60px;
    bottom: 48px;
    font-size: 11px;
    line-height: 1.4;
    text-align: right;
    font-weight: 600;
  }
</style>
</head>
<body>
  <main class="letterhead">
    <svg class="watermark" width="240" height="240" viewBox="0 0 240 240" aria-hidden="true">
      <circle cx="120" cy="120" r="110" fill="none" stroke="var(--watermark)" stroke-width="14"/>
    </svg>

    <div class="brand">
      <span class="brand-name">Bovrin-u</span>
      <span class="brand-dot"></span>
    </div>

    <address class="sender-address" style="font-style:normal">
      Level 10, 27 Harlow Lane,<br>Melbourne, Australia, 3000
    </address>
    <div class="letter-date">February 27 , 2014</div>

    <section class="letter-body">
      <p>Mr John Doe</p>
      <p>Lorem ipsum dolor sit amet, consectetuer adipiscing elit, sed diam nonummy nibh euismod tincidunt ut laoreet dolore magna aliquam erat volutpat. Ut wisi enim ad minim veniam, quis nostrud exerci tation ullamcorper suscipit lobortis nisl ut aliquip ex ea commodo consequat. Duis autem vel eum iriure dolor in hendrerit in vulputate velit esse molestie consequat, vel illum dolore eu feugiat nulla facilisis at vero eros et accumsan et iusto odio dignissim qui blandit praesent luptatum zzril delenit augue duis dolore te feugait nulla facilisi.</p>
      <p>Sed ut perspiciatis, unde omnis iste natus error sit voluptatem accusantium doloremque laudantium, totam rem aperiam eaque ipsa, quae ab illo inventore veritatis et quasi architecto beatae vitae dicta sunt, explicabo. nemo enim ipsam voluptatem, quia voluptas</p>
      <div class="signature">
        <p>Assistant Manager</p>
        <p>Jack Doe</p>
      </div>
    </section>

    <footer class="contact-footer">
      www.bovrin-u.com.au<br>
      Chirper: @bovrin_u<br>
      ProfLink: www.proflink.com/company/bovrin-u<br>
      T: +61 3 527 948 183&nbsp; F: +61 3 9042 5317
    </footer>
  </main>
</body>
</html>
```